Velvet Orchard Website A Website design for book editing

A website design for book editing

Our proofreading, editing and manuscript review packages are specifically tailored to help you publish the best possible version of your story.

NEED HELP PUBLISHING A BESTSELLER?

If you’re looking for professional book editing services from senior publishing industry insiders, look no further. Besides editing, we can also answer all your publishing questions and get you started building your author platform.

OUR SERVICES

We've carefully structured our packages to maximize value for every budget.

PRICING

$.02
PER WORD
Proofreading
Line Edit (Copy-editing)
Fix spelling and grammar
Sales copy/summary revision

$.04
PER WORD
Proofreading
Line Edit (Copy-editing)
Fix spelling and grammar
Organization and content
Plot and pacing
Manuscript Review

$.06
PER WORD
Proofreading
Line Edit (Copy-editing)
Fix spelling and grammar
Organization and content
Plot and pacing
Manuscript Review
Formatting (print and ebook)
Pre-publication proofread

OUR PROCESS

Send us a sample of your book. Our caffeine-fueled, eagle-eyed editors will go through it and then email you with their comments and suggestions. You can ask them any questions you want. They will look for…

Typos and grammatical errors.
Spelling and word choice issues
Punctuation and style
Word choice, clarity and flow.
Sentence structure and craft
If your writing is already clean, then they’ll discuss bigger picture things with you, like theme, concept, purpose, audience, potential market and branding (including title, subtitle, and tagline or elevator pitch).

Once you feel comfortable and confident in an editor’s expertise, skill and knowledge, and are ready to move ahead, we’ll send an invoice for the first half of the total word count so the editor can get started. We’ll charge the rest when the project is close to completion.

Target Market(s)

Authors

Industry/Entity Type

Book Publisher

Coding

Coded - Design and coding required

Number of Pages Required

1 page

Requirements
Must have
• OUR SERVICES
• We've carefully structured our packages to maximize value for every budget.
• PRICING
• $.02
• PER WORD
• Proofreading
• Line Edit (Copy-editing)
• Fix spelling and grammar
• Sales copy/summary revision
• $.04
• PER WORD
• Proofreading
• Organization and content
• Plot and pacing
• Manuscript Review
• $.06
• PER WORD
• Proofreading
• Plot and pacing
• Manuscript Review
• Formatting (print and ebook)
• Pre-publication proofread

```html
<!DOCTYPE html>
<html lang="en">
<head>
<meta charset="UTF-8">
<title>Velvet Orchard — Professional Proof Reading</title>
<link href="https://fonts.googleapis.com/css2?family=Poppins:wght@400;500;600&family=Lato:wght@300;400&display=swap" rel="stylesheet">
<style>
  :root {
    --hero-blue: #1f72ee;
    --hero-blue-light: #3a88f5;
    --hero-blue-deep: #1766e2;
    --white: #ffffff;
    --nav-text: rgba(255, 255, 255, 0.78);
  }
  * { margin: 0; padding: 0; box-sizing: border-box; }
  html, body {
    width: 1200px;
    height: 607px;
    overflow: hidden;
  }
  body {
    font-family: "Lato", sans-serif;
    color: var(--white);
    background: var(--hero-blue);
  }
  .hero {
    position: relative;
    width: 1200px;
    height: 607px;
    overflow: hidden;
  }
  .hero-photo {
    position: absolute;
    inset: 0;
    background:
      radial-gradient(ellipse 300px 380px at 700px 330px, var(--hero-blue-light) 0%, rgba(58,136,245,0) 100%),
      linear-gradient(180deg, var(--hero-blue-deep) 0%, var(--hero-blue) 45%, var(--hero-blue-light) 100%);
  }
  .site-header {
    position: absolute;
    top: 20px;
    left: 248px;
    right: 264px;
    height: 18px;
    display: flex;
    align-items: center;
  }
  .brand {
    display: flex;
    align-items: center;
    gap: 6px;
    font-family: "Poppins", sans-serif;
    font-weight: 500;
    font-size: 10.5px;
    color: var(--white);
    text-decoration: none;
    margin-right: 22px;
  }
  .brand-mark {
    width: 8px;
    height: 8px;
    background: var(--white);
  }
  .main-nav {
    display: flex;
    gap: 12px;
  }
  .main-nav a {
    font-family: "Lato", sans-serif;
    font-weight: 300;
    font-size: 9.5px;
    color: var(--nav-text);
    text-decoration: none;
  }
  .social-links {
    margin-left: auto;
    display: flex;
    gap: 11px;
  }
  .social-dot {
    width: 8px;
    height: 8px;
    border-radius: 50%;
    background: var(--nav-text);
  }
  .hero-content {
    position: absolute;
    left: 248px;
    top: 244px;
    width: 420px;
  }
  .hero-title {
    font-family: "Poppins", sans-serif;
    font-weight: 600;
    font-size: 37px;
    line-height: 39px;
    letter-spacing: -0.5px;
  }
  .hero-text {
    margin-top: 9px;
    font-weight: 300;
    font-size: 10px;
    line-height: 15.5px;
    width: 400px;
  }
  .btn-outline {
    display: inline-block;
    margin-top: 23px;
    width: 98px;
    height: 34px;
    line-height: 32px;
    text-align: center;
    border: 1px solid var(--white);
    border-radius: 17px;
    font-family: "Poppins", sans-serif;
    font-weight: 400;
    font-size: 11px;
    color: var(--white);
    text-decoration: none;
  }
</style>
</head>
<body>
  <section class="hero">
    <div class="hero-photo" role="img" aria-label="Photo of a smiling woman in glasses and a trench coat reading a book, tinted blue"></div>

    <header class="site-header">
      <a class="brand" href="#">
        <span class="brand-mark"></span>
        Velvet Orchard
      </a>
      <nav class="main-nav">
        <a href="#services">Our Services</a>
        <a href="#pricing">Pricing</a>
        <a href="#testimonials">Testimonials</a>
        <a href="#contact">Contact</a>
      </nav>
      <div class="social-links">
        <span class="social-dot" aria-label="Social link"></span>
        <span class="social-dot" aria-label="Social link"></span>
      </div>
    </header>

    <div class="hero-content">
      <h1 class="hero-title">Professional Proof Reading</h1>
      <p class="hero-text">Our proofreading, editing and manuscript review packages are specifically tailored to help you publish the best possible version of your story.</p>
      <a class="btn-outline" href="#services">Learn More</a>
    </div>
  </section>
</body>
</html>
```